Brackwen Timesheet App

I need a simple app for Iphone so that my employees can send me the details of where they worked and how many hours they worked for. I have a logo that will need to be integrated into it.
We will need it to also email the information to a centralized address so that the invoicing and wages can be done.
It will need to have the
Date
Mine Worked (This will have a drop down menu with 7 mines listed)
Hours Worked
Vent Report Number
Emergency Response Report Number
Surname
First Name

Target Market(s)

This app if for employees of the company, all fields will need to be filled out, but they can have either a vent report number(V/R) or and Emergency Response Report number (ERC)

Requirements
Must have

• Date
Hours Worked
Vent Report Number
Surname
First Name
Nice to have
• Ability to have app send data in email format or even to have it put into a database at a central location?

```html
<!DOCTYPE html>
<html lang="en">
<head>
<meta charset="utf-8">
<title>Brackwen Timesheet App</title>
<link href="https://fonts.googleapis.com/css2?family=Arimo:wght@400;700&display=swap" rel="stylesheet">
<style>
:root{
  --page:#e4e4e4;
  --ink:#111111;
  --caption:#222222;
  --screen-dark:#050505;
  --peach:#f6b585;
  --orange:#ff6a1f;
  --orange-deep:#e2400c;
  --field:#ffffff;
  --status-top:#3b5a5f;
  --status-bottom:#16292c;
  --key:#fdfdfd;
  --key-dark:#a9aeb8;
  --kb-top:#8e939d;
  --kb-bottom:#6a6f79;
  --search:#2b6fe0;
  --picker:#e8e8e8;
  --picker-edge:#2a2a2a;
}
*{box-sizing:border-box;margin:0;padding:0}
html,body{width:1200px;height:900px;overflow:hidden}
body{background:var(--page);font-family:"Arimo",Arial,sans-serif;color:var(--ink);position:relative}
.screen{position:absolute;top:150px;width:322px;height:487px;overflow:hidden;border-radius:2px}
.screen--front{left:45px;background:var(--screen-dark)}
.screen--entry{left:438px;background:var(--peach)}
.screen--view{left:836px;background:var(--peach)}
.step-number{position:absolute;top:18px;font-size:30px;color:var(--ink)}
.caption{position:absolute;top:806px;width:322px;text-align:center;font-size:15px;color:var(--caption);letter-spacing:.3px}

.status-bar{position:absolute;left:0;top:0;width:100%;height:20px;background:linear-gradient(var(--status-top),var(--status-bottom));color:#fff;font-size:11px;font-weight:700}
.status-bar .signal{position:absolute;left:8px;top:4px}
.status-bar .time{position:absolute;left:0;right:0;top:4px;text-align:center}
.status-bar .battery{position:absolute;right:8px;top:5px;width:22px;height:10px;border:1px solid #fff;border-radius:2px}
.status-bar .battery::after{content:"";position:absolute;left:1px;top:1px;right:1px;bottom:1px;background:#fff}

.hero-art{position:absolute;left:62px;top:36px;width:216px;height:270px;border-radius:50%;background:radial-gradient(circle at 50% 45%,#f29a3a 0%,#c4621c 35%,#3a2a1e 65%,var(--screen-dark) 80%)}
.go-button{position:absolute;left:192px;top:350px;width:93px;height:33px;border-radius:6px;background:linear-gradient(var(--orange),var(--orange-deep));color:#fff;font-weight:700;font-size:24px;text-align:center;line-height:33px}
.brand{position:absolute;left:30px;top:402px;display:flex;align-items:center;gap:10px;color:#fff;font-weight:700;font-size:27px;white-space:nowrap}
.brand-dot{width:30px;height:30px;border-radius:50%;background:#fff;flex:none}

.label{position:absolute;left:17px;font-size:11px;font-weight:700;text-transform:uppercase;line-height:13px}
.value-name{position:absolute;left:135px;top:40px;font-size:21px}
.field{position:absolute;height:30px;background:var(--field);border-radius:4px;font-size:14px;display:flex;align-items:center;justify-content:center;box-shadow:inset 0 1px 2px rgba(0,0,0,.25)}
.field--hint{font-size:11px}
.plain-value{position:absolute;font-size:14px}
.dropdown{position:absolute;left:132px;top:198px;width:180px;height:30px;background:var(--field);border-radius:4px;font-size:13px;padding-left:8px;display:flex;align-items:center}
.dropdown-arrow{position:absolute;right:0;top:0;width:30px;height:30px;border-radius:0 4px 4px 0;background:linear-gradient(var(--orange),var(--orange-deep))}
.dropdown-arrow::after{content:"";position:absolute;left:9px;top:11px;border-left:6px solid transparent;border-right:6px solid transparent;border-top:8px solid #fff}
.notes-box{position:absolute;left:20px;top:330px;width:285px;height:95px;background:var(--field);border-radius:6px;padding:14px 16px;font-size:14px;box-shadow:inset 0 1px 3px rgba(0,0,0,.3)}
.action{position:absolute;top:440px;height:33px;border-radius:6px;background:linear-gradient(var(--orange),var(--orange-deep));color:#fff;font-weight:700;font-size:13px;display:flex;align-items:center;justify-content:center}
.action--cancel{left:22px;width:86px}
.action--send{left:208px;width:92px}

.picker{position:absolute;left:0;top:112px;width:100%;height:164px;background:var(--picker-edge)}
.picker-column{position:absolute;top:0;height:164px;background:linear-gradient(#6b6b6b,var(--picker) 25%,#fff 50%,var(--picker) 75%,#6b6b6b)}
.picker-column--left{left:36px;width:124px}
.picker-column--right{left:166px;width:120px}
.picker-select{position:absolute;left:30px;top:95px;width:262px;height:42px;background:linear-gradient(rgba(255,255,255,.5),rgba(160,160,170,.45));border-top:1px solid #999;border-bottom:1px solid #999}
.picker-row{position:absolute;left:0;width:100%;text-align:center;font-size:19px;line-height:24px;z-index:2}
.picker-row--left{left:36px;width:124px}
.picker-row--right{left:166px;width:120px}

.keyboard{position:absolute;left:0;top:276px;width:100%;height:211px;background:linear-gradient(var(--kb-top),var(--kb-bottom))}
.key-row{position:absolute;left:0;width:100%;display:flex;justify-content:center;gap:4px}
.key{width:28px;height:40px;background:var(--key);border-radius:5px;font-size:18px;display:flex;align-items:center;justify-content:center;box-shadow:0 1px 0 rgba(0,0,0,.5)}
.key--function{background:var(--key-dark);color:#fff;font-size:13px}
.key--wide{width:42px}
.key--space{width:150px;font-size:14px;color:#333}
.key--search{width:74px;background:var(--search);color:#fff;font-size:14px}
</style>
</head>
<body>

<span class="step-number" style="left:8px">1</span>
<span class="step-number" style="left:400px">2</span>
<span class="step-number" style="left:798px">3</span>

<section class="screen screen--front">
  <div class="status-bar"><span class="signal">3G</span><span class="time">9:41 AM</span><span class="battery"></span></div>
  <div class="hero-art" role="img" aria-label="Illustration of a miner with a pickaxe bursting from an orange splash"></div>
  <div class="go-button">GO!</div>
  <div class="brand"><span class="brand-dot"></span><span>Brackwen pty ltd</span></div>
</section>

<section class="screen screen--entry">
  <div class="status-bar"><span class="signal">3G</span><span class="time">9:41 AM</span><span class="battery"></span></div>
  <span class="label" style="top:42px">Report from:</span>
  <span class="value-name">Liam Carver</span>
  <span class="label" style="top:88px">Vent report:</span>
  <div class="field field--hint" style="left:126px;top:78px;width:180px">CLICK TO ENTER THE #</div>
  <div class="picker">
    <div class="picker-column picker-column--left"></div>
    <div class="picker-column picker-column--right"></div>
    <div class="picker-select"></div>
    <span class="picker-row picker-row--left" style="top:-4px">2</span>
    <span class="picker-row picker-row--left" style="top:41px">3</span>
    <span class="picker-row picker-row--left" style="top:104px">4</span>
    <span class="picker-row picker-row--left" style="top:144px">5</span>
    <span class="picker-row picker-row--right" style="top:-4px">18</span>
    <span class="picker-row picker-row--right" style="top:41px">19</span>
    <span class="picker-row picker-row--right" style="top:104px">20 mins</span>
    <span class="picker-row picker-row--right" style="top:144px">21</span>
  </div>
  <div class="keyboard">
    <div class="key-row" style="top:10px">
      <span class="key">Q</span><span class="key">W</span><span class="key">E</span><span class="key">R</span><span class="key">T</span><span class="key">Y</span><span class="key">U</span><span class="key">I</span><span class="key">O</span><span class="key">P</span>
    </div>
    <div class="key-row" style="top:63px">
      <span class="key">A</span><span class="key">S</span><span class="key">D</span><span class="key">F</span><span class="key">G</span><span class="key">H</span><span class="key">J</span><span class="key">K</span><span class="key">L</span>
    </div>
    <div class="key-row" style="top:117px">
      <span class="key key--function key--wide">&#8679;</span>
      <span class="key">Z</span><span class="key">X</span><span class="key">C</span><span class="key">V</span><span class="key">B</span><span class="key">N</span><span class="key">M</span>
      <span class="key key--function key--wide">&#9003;</span>
    </div>
    <div class="key-row" style="top:165px">
      <span class="key key--function" style="width:66px">.?123</span>
      <span class="key key--space">space</span>
      <span class="key key--search">Search</span>
    </div>
  </div>
</section>

<section class="screen screen--view">
  <div class="status-bar"><span class="signal">3G</span><span class="time">9:41 AM</span><span class="battery"></span></div>
  <span class="label" style="top:42px">Report from:</span>
  <span class="value-name">Liam Carver</span>
  <span class="label" style="top:88px">Vent report:</span>
  <div class="field" style="left:132px;top:78px;width:180px">ERC16262-11281</div>
  <span class="label" style="top:132px">Hours worked:</span>
  <div class="field" style="left:132px;top:122px;width:180px">4 HR 20 MINS</div>
  <span class="label" style="top:166px">Date:</span>
  <span class="plain-value" style="left:135px;top:164px">6/17/2012</span>
  <span class="label" style="top:203px">Mine worked</span>
  <div class="dropdown">NORTH RIDGE<span class="dropdown-arrow"></span></div>
  <span class="label" style="top:247px">Emergency<br>response<br>report #</span>
  <div class="field" style="left:132px;top:246px;width:180px">XXXXX XXX XXXX</div>
  <span class="label" style="top:304px">Notes:</span>
  <div class="notes-box">I saw the light!...</div>
  <div class="action action--cancel">CANCEL</div>
  <div class="action action--send">SEND</div>
</section>

<p class="caption" style="left:45px">FRONT PAGE</p>
<p class="caption" style="left:438px">ENTERING THE DATA</p>
<p class="caption" style="left:836px">DATA PAGE VIEW</p>

</body>
</html>
```